11X17 Poster Drop A Dress Size Challenge

We are having a 21-Day Drop A Dress Size Challenge for our Fitness Studio. We need a poster designed using the template attached as a reference. I have included our Vorenzo Bootcamps logo to put in the poster as well. Please DO NOT use the graphics in the flyer as we are expecting something much better :)
- Size needed 11x17 with bleeding for printing
- We need this made in Photoshop (CS3 friendly) or at least delivered in PS as we might change some text or re-arrange the design later on.

Target Market(s)

Personal Training Studio

Industry/Entity Type

Printing

Colors
0255a3
3377b5
85acd3
f37123
f68e4e
faa54b
f78f20
0692cd
34a7d8

Requirements
Must have
• Must be 11x17 with bleed for printing
• Must be in PS file (CS3 compatible)
• Must include our Vorenzo Bootcamps logo somewhere in the poster
• Must include the information provided in the attached flyer
Nice to have
• Nice to have quality graphics that coincide with the challenge and our logo
Should not have
• Please NO scantily dressed women :)

```html
<!DOCTYPE html>
<html lang="en">
<head>
<meta charset="utf-8">
<title>Vorenzo Bootcamps – Drop a Dress Size in 21 Days</title>
<link rel="stylesheet" href="https://fonts.googleapis.com/css2?family=Catamaran:wght@300;400;500;600;700;800&display=swap">
<style>
  :root{
    --page-grey:#e6e6e6;
    --paper:#ffffff;
    --orange:#f78f20;
    --rust:#b65f12;
    --headline-brown:#8e4512;
    --ink:#1a1a1a;
    --navy:#235a8e;
    --navy-text:#1e3d60;
    --sky:#85acd3;
    --rule:#5f86ad;
    --white:#ffffff;
  }
  *{margin:0;padding:0;box-sizing:border-box}
  html,body{width:900px;height:1200px;overflow:hidden;background:var(--page-grey)}
  body{font-family:"Catamaran",Arial,sans-serif;color:var(--ink)}
  .poster{position:relative;width:900px;height:1200px}
  .sheet{position:absolute;left:62px;top:0;width:776px;height:1200px;background:var(--paper)}
  .block{position:absolute;left:83px;width:732px}

  .hero{top:25px;height:343px;background:var(--orange)}
  .hero-photo{position:absolute;left:0;top:0;width:457px;height:343px;
    background:linear-gradient(180deg,#d9a07a 0%,#c98a64 55%,#35577f 78%,#2d4a6e 100%)}
  .brand{position:absolute;right:10px;top:10px;font-weight:800;font-size:22px;color:var(--navy-text);letter-spacing:.5px}
  .headline{position:absolute;font-weight:700;color:var(--headline-brown);line-height:1}
  .headline.drop{left:357px;top:72px;font-size:56px}
  .headline.dress{left:437px;top:132px;font-size:56px}
  .headline.in{left:357px;top:183px;font-size:40px}
  .days-box{position:absolute;left:465px;top:217px;width:267px;height:70px;background:var(--ink);
    color:var(--white);font-weight:700;font-size:52px;line-height:70px;text-align:center}
  .days-box em{font-style:italic;font-weight:600}

  .band{background:var(--rust);color:var(--white);font-weight:300;text-align:center}
  .band.intro{top:368px;height:50px;font-size:27px;line-height:52px}

  .offer{top:418px;height:434px;background:var(--sky)}
  .pain{position:absolute;left:9px;top:7px;width:313px;height:340px;background:var(--navy);
    color:var(--white);font-size:17px;line-height:21px;padding:12px 14px 0 16px}
  .pain p+p{margin-top:21px}
  .start{position:absolute;left:9px;top:350px;width:313px;height:60px;background:var(--orange);
    font-size:30px;font-weight:500;line-height:62px;text-align:center}
  .start sup{font-size:16px}
  .benefits{position:absolute;left:337px;top:12px;width:378px;color:var(--navy-text);font-size:18.5px;line-height:23px}
  .benefits h2{font-size:19px;font-weight:700;margin-bottom:10px}
  .benefits li{list-style:none;border-bottom:1px solid var(--rule);padding:0 0 6px;margin-bottom:6px}
  .benefits li:last-child{border:none}
  .benefits b{font-weight:700}

  .band.value{top:852px;height:36px;font-size:27px;line-height:40px}

  .claim{top:888px;height:97px;background:var(--orange);text-align:center;color:var(--rust)}
  .claim .cta{font-size:18px;font-weight:500;padding-top:27px;line-height:22px}
  .claim .contact{font-size:26px;font-weight:700;line-height:34px}

  .prize{top:985px;height:140px;background:var(--navy);color:var(--white)}
  .prize .left{position:absolute;left:22px;top:20px;font-size:28px;line-height:31px;font-weight:400}
  .prize .right{position:absolute;right:22px;top:20px;font-size:28px;line-height:31px;text-align:right}
  .prize b{font-weight:700}
  .prize small{font-size:22px;font-weight:300;color:#c7d7ea}
  .winner{position:absolute;left:292px;top:2px;width:148px;height:148px;border-radius:50%;background:var(--orange);
    color:var(--ink);font-weight:700;font-size:25px;line-height:30px;text-align:center;padding-top:44px}

  .hurry{top:1125px;height:45px;background:var(--orange);font-size:32px;font-weight:500;text-align:center;line-height:50px;letter-spacing:.5px}
</style>
</head>
<body>
<div class="poster">
  <div class="sheet"></div>

  <section class="block hero">
    <div class="hero-photo" role="img" aria-label="Photo of a slim waist in loosened jeans, showing a dropped size"></div>
    <div class="brand">VORENZO BOOTCAMPS</div>
    <h1>
      <span class="headline drop">Drop a</span>
      <span class="headline dress">dress size</span>
      <span class="headline in">in</span>
      <span class="days-box"><em>21</em> days</span>
    </h1>
  </section>

  <div class="block band intro">If so, then this amazing offer is perfect for you…</div>

  <section class="block offer">
    <div class="pain">
      <p>Are you tired of all the health clubs and fitness centers that tell you exactly what you want to hear to get you to join, but once you’re a member they forget about you and don’t teach you anything about how to get results?</p>
      <p>Are you frustrated by all the gimmicks; the pills, powders, shakes and gadgets sold on late night TV that are nothing more than empty promises and slick marketing?</p>
    </div>
    <div class="start">Starts April 6<sup>th</sup> 2015</div>
    <div class="benefits">
      <h2>Here’s what you get:</h2>
      <ul>
        <li>Three weeks worth of <b>Fat Burning Work-outs</b> with a Certified Personal Trainer to make sure that you don’t spend one minute exercising that doesn’t produce results.</li>
        <li><b>21 Days of Fat Burning Meal Plans</b> designed by a Registered Dietician to ensure that you reach your goals as quickly as possible.</li>
        <li><b>Nutrition Coaching Session</b> to answer all your questions and set you up for</li>
        <li><b>21 Days of Lessons</b> to keep you on track to achieving your goal of dropping a dress size</li>
      </ul>
    </div>
  </section>

  <div class="block band value">…You get all this – a $327 Value - for ONLY $97!</div>

  <section class="block claim">
    <p class="cta">CLAIM YOUR SPOT NOW</p>
    <p class="contact">www.Vorenzobootcamps.com/Call 303-555-0147</p>
  </section>

  <section class="block prize">
    <p class="left"><b>$100</b> Cash,<br>A NEW DRESS<br><small>(Up to $100 Value)</small></p>
    <div class="winner">WINNER<br>GETS</div>
    <p class="right">And A Free<br><b>PHOTO SHOOT!</b><br><small>($150 Value)</small></p>
  </section>

  <div class="block hurry">HURRY!&nbsp; SPACE IS LIMITED LADIES!!</div>
</div>
</body>
</html>
```